Design a flyer

Hi, I need a flyer designed for an electrical and air conditioning company based in brisbane, Australia.
We service the domestic market.
Flyer is to be double sided
Flyer size DL 210mm X 99mm
Was thinking one side services and discount coupons and the other side possible testimonials.
I have logo uploaded followed with the vehicle advertising, advertising stand alone sign and also business cards.
--------------------------
Coupon Cut out
save $150 OFF switchboard upgrades
save $150 Complimentary Electrical safety inspection
save $50 OFF Air Conditioner install or Service
save $50 next job if you leave feedback for first job
OVER $400 WORTH OF SAVINGS!
Our promise to you
* we will Arrive on time or we will pay you $100
* Before any job begins you will know the exact price
* We will leave your place as clean as we arrived
* if there is a problem and its our fault we will fix it for free
* provide a 12 month warranty on all parts
* we will provide friendly helpful service and advice
Phone number is 0487 625 903
Company Name - Tavolinex
License: 58164
ABN - 61 208 395 172
Also add vornel pay, zund and paklin logo at the bottom
----------------------------
Here is what some of my customers have had to say
Extremely professional...
“Arrived when he said he would, sent through a written quote and was very reasonable. He also checked out our smoke
detectors whist he was here. He installed 2 ceiling fans and an air conditioner. He
cleaned up the mess and was very efficient. I will definitely use him again and recommend
him to family and friends”
R.M – Stretton
“Excellent service provider. He arrived on time with a call before arriving, than carried all jobs quickly and efficiently and left no mess at all. I will definitely recommend his service to others requiring an electrician. Thanks again!”
K.S – Greenslopes
“Over the long weekend, I had problems with my power, not only did you pick up the first phone call but you came out at 5am to fix it. Love the fact you’re a 24hr service!”
T.W – Mount Gravatt
---------------------------
NEW changes
Hi everyone,
Just want to say well done all the designers look great!
I will soon be choosing a winner, but there are a couple of changes i would like to make, if you revise you will be in for a win.
Instead of Save 50 if you leave feedback for the first job quote. I want to change that put $110 cross out and put $71.50 Install & Supply LED Downlights (min 20)
I want this to be the number one followed by switch board upgrade cut out.
Also $50 off air con install - don't put service.
And the third testimonial T.W Make sure it has a full stop
Also keep in mind. It is an electrical & air conditioning company.
Be creative with your design, don't want to see any pictures of people as they are not working for us at this time.
Remember key focus, on coupons, phone numbers, and website. zund and vornelpay can be small and out of the way same with the license numbers.
Thank you
Good Luck!
Target Market(s)
Domestic Market - Home owners
Industry/Entity Type
Air Conditioning

```html
<!DOCTYPE html>
<html lang="en">
<head>
<meta charset="utf-8">
<title>Tavolinex DL Flyer</title>
<link href="https://fonts.googleapis.com/css2?family=Source+Sans+3:wght@400;600;700&display=swap" rel="stylesheet">
<style>
  :root{
    --orange:#e8672a;
    --panel:#f4f4f4;
    --white:#ffffff;
    --blue:#1f6db4;
    --green:#2b9a33;
    --grey:#9a9a9a;
    --bullet:#b3b3b3;
    --ink:#1a1a1a;
  }
  *{box-sizing:border-box;margin:0;padding:0}
  html,body{width:1200px;height:318px;overflow:hidden;background:var(--white)}
  body{position:relative;font-family:"Source Sans 3",Arial,sans-serif;color:var(--ink)}

  .flyer-side{position:absolute;top:12px;height:296px;background:var(--orange)}
  .front{left:10px;width:587px}
  .back{left:613px;width:579px}

  .front-panel{position:absolute;left:8px;top:10px;width:570px;height:240px;background:var(--panel)}
  .back-panel{position:absolute;left:10px;top:10px;width:562px;height:276px;background:var(--white)}

  .brand{position:absolute;left:2px;top:20px;display:flex;align-items:center;gap:8px}
  .brand-mark{width:13px;height:13px;border-radius:50%;background:var(--orange)}
  .brand-name{font-size:38px;font-weight:400;color:var(--blue);letter-spacing:.5px;line-height:40px}

  .services-title{position:absolute;left:255px;top:24px;width:290px;text-align:center;
    font-size:21px;font-weight:700;color:var(--grey);line-height:28px}

  .coupon-title{position:absolute;left:-4px;top:84px;font-size:20px;line-height:24px;font-weight:700;color:var(--green)}
  .coupon-list{position:absolute;left:-3px;top:113px;list-style:none}
  .coupon-list li{display:flex;align-items:center;gap:6px;height:22px;
    font-size:12.5px;font-weight:700;color:var(--orange);white-space:nowrap}
  .coupon-list li::before{content:"";flex:none;width:11px;height:11px;border-radius:50%;background:var(--bullet)}
  .savings{position:absolute;left:0;top:212px;font-size:19px;line-height:22px;font-weight:700;color:var(--blue)}

  .promise{position:absolute;left:322px;top:104px}
  .promise-title{font-size:13px;line-height:16px;font-weight:700;margin-bottom:2px}
  .promise-list{list-style:none}
  .promise-list li{font-size:8.3px;font-weight:700;line-height:16px;white-space:nowrap}

  .footer-band{position:absolute;left:0;top:250px;width:587px;height:46px;color:var(--white)}
  .licence{position:absolute;left:20px;top:1px;font-size:8px;font-weight:600;line-height:15px}
  .phone{position:absolute;left:155px;top:-1px;font-size:32px;line-height:36px;font-weight:700;letter-spacing:1px}
  .payments{position:absolute;left:405px;top:8px;display:flex;gap:8px}
  .pay-option{display:flex;align-items:center;gap:3px;font-size:10.5px;font-weight:700;color:var(--white)}
  .pay-option::before{content:"";width:9px;height:9px;background:var(--white)}

  .testimonials-title{position:absolute;left:12px;top:9px;font-size:21px;line-height:26px;font-weight:700;color:var(--blue);white-space:nowrap}
  .testimonials{position:absolute;left:13px;top:34px;width:545px;font-size:9.8px;line-height:16.5px;white-space:nowrap}
  .testimonial{margin-bottom:8px}
</style>
</head>
<body>
  <section class="flyer-side front">
    <div class="front-panel">
      <div class="brand"><span class="brand-mark"></span><span class="brand-name">Tavolinex</span></div>
      <h2 class="services-title">Electrical &amp; Air Conditioning Services</h2>

      <h3 class="coupon-title">Coupon Cut Out</h3>
      <ul class="coupon-list">
        <li>Save $150 OFF switchboard upgrades</li>
        <li>Save $150 Complimentary Electrical safety inspection</li>
        <li>save $50 OFF Air Conditioner install or Service</li>
        <li>save $50 next job if you leave feedback for first job</li>
      </ul>
      <p class="savings">OVER $400 WORTH OF SAVINGS!</p>

      <div class="promise">
        <h3 class="promise-title">Our promise to you</h3>
        <ul class="promise-list">
          <li>* we will Arrive on time or we will pay you $100</li>
          <li>* Before any job begins you will know the exact price</li>
          <li>* We will leave your place as clean as we arrived</li>
          <li>* if there is a problem and its our fault we will fix it for free</li>
          <li>* provide a 12 month warranty on all parts</li>
          <li>* we will provide friendly helpful service and advice</li>
        </ul>
      </div>
    </div>

    <div class="footer-band">
      <p class="licence">License: 58164<br>ABN - 61 208 395 172</p>
      <p class="phone">0487 625 903</p>
      <div class="payments">
        <span class="pay-option">vornelpay</span>
        <span class="pay-option">zund</span>
        <span class="pay-option">paklin</span>
      </div>
    </div>
  </section>

  <section class="flyer-side back">
    <div class="back-panel">
      <h2 class="testimonials-title">Here is what some of my customers have had to say</h2>
      <div class="testimonials">
        <p class="testimonial">Extremely professional...<br>
          “Arrived when he said he would, sent through a written quote and was very reasonable. He also checked out our smoke<br>
          detectors whist he was here. He installed 2 ceiling fans and an air conditioner. He<br>
          cleaned up the mess and was very efficient. I will definitely use him again and recommend<br>
          him to family and friends”<br>
          R.M – Stretton</p>
        <p class="testimonial">“Excellent service provider. He arrived on time with a call before arriving, than carried all jobs quickly and efficiently and<br>
          left no mess at all. I will definitely recommend his service to others requiring an electrician. Thanks again!”<br>
          K.S – Greenslopes</p>
        <p class="testimonial">“Over the long weekend, I had problems with my power, not only did you pick up the first phone call but you came out at<br>
          5am to fix it. Love the fact you’re a 24hr service!”<br>
          T.W – Mount Gravatt</p>
      </div>
    </div>
  </section>
</body>
</html>
```